Book Cover - For Best Selling Diet

Hi
Book cover required for a diet book being marketed to become a best seller
For best quality, image will be 2820 pixels on the shortest side and 4500 pixels on the longest side .
The book name : Bright Morning Plan
By Marisol Penhale
( will add in the extra text once we see design - top and bottom subtitle )
I do not want a photo of a person on the book.
PLEASE SEE " THE NINE STEP CORE" by Dale Whitcombe as an example of solid style and I also love Quiet Lantern for the font.
Branding Colours:
#F26432
#A4195C
#A7D8CC
Font that runs through our brand is : helvetica neue
This is for a book that will be marketed for #1 bestseller - So please only quality
designs that are designed in a unique style.
Thanks
Target Market(s)
Busy Working Mums, Affluent, 30+ .
Look and feel

```html
<!DOCTYPE html>
<html lang="en">
<head>
<meta charset="utf-8">
<title>Bright Morning Plan — Book Cover</title>
<link rel="stylesheet" href="https://fonts.googleapis.com/css2?family=Inter:wght@100;200;300&display=swap">
<style>
  :root {
    --paper: #ffffff;
    --brand-orange: #F26432;
    --brand-plum: #A4195C;
    --brand-mint: #A7D8CC;
    --brand-coral: #E8413A;
    --brand-sand: #C9B48E;
  }
  * { margin: 0; padding: 0; box-sizing: border-box; }
  html, body {
    width: 930px;
    height: 1200px;
    overflow: hidden;
    background: var(--paper);
  }
  .cover {
    position: relative;
    width: 930px;
    height: 1200px;
    background: var(--paper);
    font-family: "Inter", "Helvetica Neue", Helvetica, Arial, sans-serif;
    text-align: center;
  }
  .cover__line {
    position: absolute;
    left: 0;
    width: 100%;
    -webkit-background-clip: text;
    background-clip: text;
    color: transparent;
    white-space: nowrap;
  }
  .cover__kicker {
    top: 340px;
    font-size: 58px;
    font-weight: 200;
    letter-spacing: 1px;
    line-height: 1;
    background-image: linear-gradient(90deg, var(--brand-orange), var(--brand-coral) 45%, var(--brand-plum));
  }
  .cover__title {
    top: 395px;
    font-size: 300px;
    font-weight: 100;
    letter-spacing: -4px;
    line-height: 1;
    background-image: linear-gradient(180deg, var(--brand-mint) 12%, var(--brand-sand) 42%, var(--brand-orange) 68%, var(--brand-coral) 90%);
  }
  .cover__by {
    top: 755px;
    font-size: 62px;
    font-weight: 200;
    line-height: 1;
    background-image: linear-gradient(90deg, var(--brand-coral), var(--brand-plum));
  }
  .cover__author {
    top: 860px;
    font-size: 68px;
    font-weight: 200;
    line-height: 1;
    background-image: linear-gradient(90deg, var(--brand-coral), var(--brand-plum) 70%, var(--brand-coral));
  }
</style>
</head>
<body>
  <main class="cover">
    <h1>
      <span class="cover__line cover__kicker">BRIGHT MORNING</span>
      <span class="cover__line cover__title">Plan</span>
    </h1>
    <p class="cover__line cover__by">BY</p>
    <p class="cover__line cover__author">Marisol Penhale</p>
  </main>
</body>
</html>
```